Electrical business needs a flyer design

we need a Trifold flyer designed for an electrical company. Our service include new installations, renovations and rewires, safety checks, switchboard upgrades, services and breakdown, home automation and power monitoring. we would like to see designs using dark grey, orange and blue. the final designs should communicate a friendly but professional service. I have attached my old business brochure to indicate the service we provide
Target Market(s)
home owners
Industry/Entity Type
Electrical
Look and feel
Each slider illustrates characteristics of the customer's brand and the style your logo design should communicate.

```html
<!DOCTYPE html>
<html lang="en">
<head>
<meta charset="utf-8">
<title>Ridgeline Electrical – Trifold Brochure</title>
<link href="https://fonts.googleapis.com/css2?family=Montserrat:wght@700;800&family=Roboto:wght@400&family=Didact+Gothic&display=swap" rel="stylesheet">
<style>
  :root{
    --blue:#0a8fd3;
    --blue-deep:#1a6fbf;
    --orange:#f7731a;
    --ink:#1d1d1d;
    --rule:#3fd3e6;
    --paper:#ffffff;
    --backdrop:#c9c9c9;
  }
  *{margin:0;padding:0;box-sizing:border-box}
  html,body{width:1200px;height:800px;overflow:hidden;background:var(--backdrop)}
  .brochure{position:absolute;left:50px;top:10px;width:1100px;height:780px;background:var(--paper);display:flex}
  .panel{position:relative;height:100%}
  .panel--services{width:361px}
  .panel--about{width:367px;border-left:1px solid var(--rule);border-right:1px solid var(--rule)}
  .panel--cover{width:372px}
  .base-band{position:absolute;left:0;right:0;bottom:0;height:16px;background:var(--blue)}
  .body-copy{position:absolute;font-family:"Roboto",sans-serif;font-size:13.6px;line-height:15.6px;color:var(--ink)}
  .pill{position:absolute;height:21px;background:var(--blue);border-radius:2px;color:#fff;
    font-family:"Montserrat",sans-serif;font-weight:700;font-size:12.5px;line-height:21px;text-align:center;letter-spacing:.2px}
  .photo{position:absolute;width:260px;height:260px;border-radius:50%;border:3px solid var(--blue)}
  .photo--electrician{left:49px;top:260px;background:radial-gradient(circle at 35% 45%,#e9d7c7 0 18%,#c9ccd0 30%,#8e9aa5 60%,#5b6b7a)}
  .photo--switchboard{left:53px;top:260px;background:linear-gradient(160deg,#d8dcc0 0%,#b9c66a 25%,#3a7fc0 55%,#e6e8ea 75%,#9aa3ab)}
  .contact{position:absolute;left:30px;top:610px;font-family:"Didact Gothic",sans-serif;font-size:14px;line-height:15.8px;color:var(--ink)}
  .contact .row{display:flex}
  .contact .label{width:58px}
  .brand{position:absolute;left:0;right:0;top:112px;display:flex;align-items:center;justify-content:center;gap:10px}
  .brand-dot{width:22px;height:22px;border-radius:50%;background:var(--orange)}
  .brand-name{font-family:"Montserrat",sans-serif;font-weight:800;font-size:24px;color:var(--blue-deep);letter-spacing:.3px}
  .hero-mark{position:absolute;left:33px;top:237px;width:306px;height:306px}
  .tagline{position:absolute;left:0;right:0;top:556px;text-align:center;font-family:"Montserrat",sans-serif;font-weight:800;font-size:21px;line-height:25px;color:var(--blue-deep)}
  .tagline .accent{color:var(--orange)}
  .accreditation{position:absolute;left:132px;top:700px;width:40px;height:44px;background:var(--orange);border-radius:3px}
</style>
</head>
<body>
<main class="brochure">
  <section class="panel panel--services">
    <p class="body-copy" style="left:25px;top:75px;width:330px">We offer a 24-hour, seven-day emergency response service where you need an electrician due to a breakdown or other disruption to your power supply. Our electrical contractors will identify the fault and have your power back on as soon as possible.</p>
    <div class="photo photo--electrician" role="img" aria-label="Photo of an electrician in a hard hat testing a switchboard"></div>
    <h2 class="pill" style="left:60px;top:551px;width:250px">ACCREDITED MASTER ELECTRICIAN</h2>
    <p class="body-copy" style="left:18px;top:589px;width:335px">Elecrical work is one of the most dangerous tasks that can be performed in a home or business. every year, dozens of people are business. every year, dozens of people are electrocutedor shocked by substandard electrical work. by choosing a master electrician, you are choosing a contractor whose safety systems are accredited and monitored, and who provides excellent servies and information, potentially saving you time and money.</p>
    <div class="base-band"></div>
  </section>

  <section class="panel panel--about">
    <h2 class="pill" style="left:72px;top:26px;width:221px">ABOUT US</h2>
    <p class="body-copy" style="left:19px;top:75px;width:340px">R T Vale Electrical is a privately owned business provi -ding a comprehensive range of domestic, commercial and industrial electrical services.<br><br>We provide a comprehensive range of electrical and communication services including small jobs around the home to large industrial applications. Our businessis underpinned by a commitment to customer service, that is, we turn up on time providing quality workmanship at a fair and competiive price.</p>
    <div class="photo photo--switchboard" role="img" aria-label="Photo of switchboard wiring with coloured cables and circuit breakers"></div>
    <h2 class="pill" style="left:69px;top:551px;width:221px">CONTACT INFORMATION</h2>
    <div class="contact">
      <p>Ray Vale</p>
      <p class="row" style="margin-top:4px"><span class="label">Address</span>: PO Box 418 Harbour Vale SA 5999</p>
      <p class="row"><span class="label">Phone</span>: 0400 555 012</p>
      <p class="row"><span class="label">Fax</span>: 8600 0000</p>
      <p class="row"><span class="label">Email</span>: rtvaleelectrical@example.com</p>
    </div>
    <div class="base-band"></div>
  </section>

  <section class="panel panel--cover">
    <div class="brand">
      <span class="brand-dot"></span>
      <span class="brand-name">RIDGELINE ELECTRICAL</span>
    </div>
    <svg class="hero-mark" viewBox="0 0 306 306" role="img" aria-label="Illustration of a light bulb with an electric plug inside an orange ring">
      <defs>
        <radialGradient id="glow" cx="50%" cy="45%" r="55%">
          <stop offset="0" stop-color="#fde3c6"/>
          <stop offset="1" stop-color="#f7a25a"/>
        </radialGradient>
      </defs>
      <circle cx="153" cy="153" r="150" fill="url(#glow)"/>
    </svg>
    <p class="tagline">FOR ALL YOUR<br><span class="accent">ELECTRICAL</span> NEEDS</p>
    <div class="accreditation" role="img" aria-label="Accreditation badge"></div>
    <div class="base-band"></div>
  </section>
</main>
</body>
</html>
```